the look of import selling star-up company

I have attached rhino logo that i like (can be edit) and i wanna turn that in to luxury look. Example like black base and gold logo +luxury looking font.

Company name: Brevan trading Oy
Slogan: Beyond the everyday finish.
CEO Juho Kettumaa
Starting to import ceramic nano coatings to cars, in home use and industrial purposes.

Target Market(s)

30-60 year old men and women ho have big money and know what car they drive

Industry/Entity Type

It Company

```html
<!DOCTYPE html>
<html lang="en">
<head>
<meta charset="utf-8">
<title>Brevan trading Oy — Stationery</title>
<link href="https://fonts.googleapis.com/css2?family=Montserrat:wght@400;600;700&family=Arimo:wght@400;700&display=swap" rel="stylesheet">
<style>
  :root{
    --bg:#e6e7e9;
    --paper:#ffffff;
    --ink:#111111;
    --muted:#555555;
    --gold:#d4a514;
    --gold-deep:#b38a0c;
    --card:#0b0b0b;
  }
  *{box-sizing:border-box;margin:0;padding:0}
  html,body{width:1200px;height:960px;overflow:hidden;background:var(--bg)}
  body{position:relative;font-family:"Arimo",Arial,sans-serif;color:var(--ink)}

  .brand{display:flex;flex-direction:column;align-items:center;gap:6px}
  .brand-mark{width:62px;height:62px;border-radius:50%;background:radial-gradient(circle at 35% 30%,#f3d55a,var(--gold) 55%,var(--gold-deep))}
  .brand-name{font-family:"Montserrat",sans-serif;font-weight:700;font-size:17px;letter-spacing:.14em;text-transform:uppercase;color:var(--ink)}
  .brand-slogan{font-family:"Montserrat",sans-serif;font-size:7px;letter-spacing:.18em;text-transform:uppercase;color:var(--muted)}

  /* Letterhead */
  .letterhead{position:absolute;left:60px;top:36px;width:540px;height:740px;background:var(--paper);box-shadow:0 2px 10px rgba(0,0,0,.12);padding:44px 48px}
  .letterhead .brand{margin-bottom:34px}
  .salutation{font-weight:700;font-size:11px;margin-bottom:14px;letter-spacing:.04em}
  .letter-body p{font-size:10.5px;line-height:1.45;margin-bottom:12px;letter-spacing:.02em}
  .letter-footer{position:absolute;left:40px;bottom:44px;display:flex;align-items:flex-end;gap:20px}
  .footer-dot{width:52px;height:52px;border-radius:50%;background:var(--ink);flex:none}
  .footer-block{font-family:"Montserrat",sans-serif;font-size:8.5px;line-height:1.6;letter-spacing:.06em;text-transform:uppercase;white-space:nowrap}
  .footer-block strong{font-weight:700}

  /* Envelope */
  .envelope{position:absolute;left:470px;top:600px;width:690px;height:330px;background:var(--paper);box-shadow:0 2px 10px rgba(0,0,0,.14);overflow:hidden}
  .envelope .brand{position:absolute;left:40px;top:28px}
  .envelope .brand-mark{width:56px;height:56px}
  .envelope .brand-name{font-size:15px}
  .envelope-window{position:absolute;left:40px;top:150px;width:250px;height:120px;border:1px solid #bdbdbd;border-radius:12px;background:#f7f7f7}
  .envelope-corner{position:absolute;right:-70px;bottom:-90px;width:240px;height:240px;border-radius:50%;border:14px solid var(--ink)}

  /* Business cards */
  .card{position:absolute;width:290px;height:165px;background:var(--card);border-radius:6px;box-shadow:0 3px 10px rgba(0,0,0,.3);color:#fff}
  .card-front{left:860px;top:120px}
  .card-frame{position:absolute;inset:10px;border:1px solid var(--gold-deep);border-radius:3px}
  .card-front .brand{position:absolute;inset:0;justify-content:center}
  .card-front .brand-mark{width:64px;height:64px}
  .card-front .brand-name{font-size:11px;font-weight:700;color:#cfcfcf}
  .card-front .brand-slogan{font-size:5.5px;color:#9a9a9a}

  .card-back{left:860px;top:320px;overflow:hidden}
  .card-back::before,.card-back::after{content:"";position:absolute;left:0;width:110px;height:3px;background:var(--gold)}
  .card-back::before{top:0}
  .card-back::after{bottom:0}
  .card-contact{position:absolute;left:18px;top:20px;font-family:"Montserrat",sans-serif}
  .card-contact .name{font-size:11px;font-weight:700;letter-spacing:.08em}
  .card-contact .role{font-size:8px;font-weight:600;color:var(--gold);margin-bottom:10px}
  .card-contact dl{font-size:6.5px;line-height:1.7;color:#d9d9d9}
  .card-contact dt{display:inline;font-weight:700}
  .card-contact dd{display:inline}
  .card-contact dd::after{content:"";display:block}
  .card-dot{position:absolute;right:26px;top:50%;transform:translateY(-50%);width:74px;height:74px;border-radius:50%;background:#fff}
</style>
</head>
<body>

<article class="letterhead">
  <header class="brand">
    <div class="brand-mark" aria-hidden="true"></div>
    <div class="brand-name">Brevan trading Oy</div>
    <div class="brand-slogan">Beyond the everyday finish</div>
  </header>

  <p class="salutation">Dear Mr. Juho Kettumaa</p>
  <div class="letter-body">
    <p>This page shows how a letter sits on the company letterhead. The text here is only a placeholder that fills the space a real message would take, so that line length, spacing and the balance of the page can be judged before any final wording is written. A finished letter would replace these lines with the actual message, keeping the same margins and the same quiet, even rhythm from the greeting down to the closing lines of the page.</p>
    <p>The body copy is set in a plain sans serif at a modest size so that it reads easily and leaves the gold mark at the top to carry the identity. Paragraphs are separated by a little space rather than indents, which keeps the left edge clean. Longer letters continue in the same way, with each new paragraph following the last and no extra decoration in between. The footer holds the name, the role and the contact lines, and it stays in the same place on every page so that the reader always knows where to find them when a reply is needed.</p>
    <p>A short final paragraph closes the letter. It may thank the reader, confirm a date or offer a next step, and it is followed by the sender's details in the footer below, set in small capitals to match the rest of the set.</p>
  </div>

  <footer class="letter-footer">
    <div class="footer-dot" aria-hidden="true"></div>
    <div class="footer-block"><strong>CEO</strong><br>Juho Kettumaa</div>
    <div class="footer-block"><strong>Call</strong> - 040-5521-370<br><strong>Mail</strong> - brevantrading.fi</div>
  </footer>
</article>

<section class="envelope">
  <div class="brand">
    <div class="brand-mark" aria-hidden="true"></div>
    <div class="brand-name">Brevan trading Oy</div>
    <div class="brand-slogan">Beyond the everyday finish</div>
  </div>
  <div class="envelope-window" aria-hidden="true"></div>
  <div class="envelope-corner" aria-hidden="true"></div>
</section>

<section class="card card-front">
  <div class="card-frame" aria-hidden="true"></div>
  <div class="brand">
    <div class="brand-mark" aria-hidden="true"></div>
    <div class="brand-name">Brevan trading Oy</div>
    <div class="brand-slogan">Beyond the everyday finish</div>
  </div>
</section>

<section class="card card-back">
  <div class="card-contact">
    <div class="name">Juho Kettumaa</div>
    <div class="role">CEO</div>
    <dl>
      <dt>Call</dt> <dd>- 040-5521-370</dd>
      <dt>Fax</dt> <dd>- 040-5521-371</dd>
      <dt>Web</dt> <dd>- www.brevantrading.fi</dd>
      <dt>Mail</dt> <dd>- brevantrading.fi</dd>
      <dt>Add</dt> <dd>- Your floor, Your street, Helsinki-00180</dd>
    </dl>
  </div>
  <div class="card-dot" aria-hidden="true"></div>
</section>

</body>
</html>
```